Maple 3 Adjustable Pillow Package Design

I need a package design for our Maple 3 Adjustable Memory Foam Pillow. We offer comfort solutions that will help you live a pain-free, healthier & happier life. Our name Maple 3 means a state of bliss, elation or happiness. We will capitalize on the popularity of the term “On Maple 3” by selling the emotion of contented happiness that comes from owning our products. Our products improve the lives of our customers and we will market that by creating experiences that are memorable and keep people coming back. I have attached the template (print area) that must be followed.

Industry/Entity Type

Health & Wellness

Colors
0054AA
0677BA
7BADD7
CADEEF
E8F1F8

Requirements
Nice to have
• I have attached a few different examples.

```html
<!DOCTYPE html>
<html lang="en">
<head>
<meta charset="utf-8">
<title>Maple 3 Adjustable Pillow – Package Front</title>
<link href="https://fonts.googleapis.com/css2?family=Exo+2:ital,wght@1,300&family=Montserrat:wght@300;500;700&family=Oswald:wght@500;600&display=swap" rel="stylesheet">
<style>
  :root {
    --navy: #022548;
    --blue-deep: #0054AA;
    --blue: #0677BA;
    --blue-bright: #0a9ce0;
    --blue-soft: #7BADD7;
    --blue-pale: #CADEEF;
    --blue-mist: #E8F1F8;
    --black: #050505;
    --white: #ffffff;
  }
  * { margin: 0; padding: 0; box-sizing: border-box; }
  html, body { width: 1200px; height: 873px; overflow: hidden; background: var(--white); }
  .canvas { position: relative; width: 1200px; height: 873px; background: var(--white); }

  .package-front {
    position: absolute; left: 418px; top: 24px;
    width: 660px; height: 1460px;
    transform: scale(0.565); transform-origin: 0 0;
  }

  .tagline-panel {
    position: absolute; left: 17px; top: 20px; width: 440px; height: 305px;
    background: linear-gradient(100deg, var(--blue-deep), var(--blue) 60%, var(--blue-bright));
    border-radius: 16px; transform: rotate(1deg);
  }
  .tagline {
    position: absolute; left: 48px; top: 50px; color: var(--white);
    font-family: "Exo 2", sans-serif; font-style: italic; font-weight: 300;
    line-height: 0.95; white-space: nowrap;
  }
  .tagline .small { font-size: 40px; display: block; }
  .tagline .large { font-size: 66px; display: block; letter-spacing: -1px; }
  .tagline-rule { position: absolute; left: 48px; top: 228px; }

  .photo-hero {
    position: absolute; left: 300px; top: 5px; width: 310px; height: 365px;
    background: linear-gradient(160deg, #d9d6d4 0%, #f3f3f3 45%, #b9a8a6 100%);
    border-radius: 40px 0 0 0;
  }
  .photo-cloud {
    position: absolute; left: 0; top: 325px; width: 320px; height: 145px;
    background: radial-gradient(ellipse at 60% 60%, #f4f4f4 0%, #dcdcdc 55%, rgba(255,255,255,0) 75%);
  }

  .main-panel {
    position: absolute; left: 70px; top: 470px; width: 540px; height: 985px;
    background: var(--navy); border-radius: 0 0 16px 10px;
    transform: skewY(0.6deg);
  }

  .logo-panel {
    position: absolute; left: 182px; top: 360px; width: 458px; height: 275px;
    background: linear-gradient(90deg, var(--blue-bright), var(--blue) 70%, #1a73b8);
    border-radius: 16px; transform: rotate(-1.8deg);
    display: flex; flex-direction: column; align-items: center; justify-content: center;
    color: var(--white);
  }
  .brand-name { font-family: "Oswald", sans-serif; font-weight: 600; font-size: 96px; line-height: 1; margin-top: 20px; white-space: nowrap; }
  .brand-sub { font-family: "Montserrat", sans-serif; font-weight: 700; font-size: 26px; margin-top: 10px; }

  .product-title {
    position: absolute; left: 70px; top: 660px; width: 540px; text-align: center;
    font-family: "Montserrat", sans-serif; font-weight: 500; color: var(--white);
    font-size: 76px; line-height: 0.9; letter-spacing: 1px;
  }

  .feature-list { position: absolute; left: 50px; top: 820px; width: 580px; list-style: none; }
  .feature { position: relative; height: 94px; padding-left: 85px; white-space: nowrap; }
  .feature-icon {
    position: absolute; left: 0; top: 4px; width: 60px; height: 60px; border-radius: 50%;
    background: var(--blue); border: 3px solid var(--blue-soft);
    display: flex; align-items: center; justify-content: center;
  }
  .feature-title {
    font-family: "Oswald", sans-serif; font-weight: 500; color: var(--white);
    font-size: 38px; line-height: 1.05; font-variant: small-caps; letter-spacing: 0.3px;
  }
  .feature-text { font-family: "Montserrat", sans-serif; font-weight: 300; color: var(--white); font-size: 18px; }

  .size-tag {
    position: absolute; left: 28px; top: 1232px; width: 275px; height: 108px;
    background: var(--black); transform: skewX(-3deg) rotate(1deg);
    color: var(--white); text-align: center; white-space: nowrap;
  }
  .size-name { font-family: "Oswald", sans-serif; font-weight: 500; font-size: 52px; line-height: 1; margin-top: 14px; display: block; }
  .size-dims { font-family: "Montserrat", sans-serif; font-weight: 300; font-size: 34px; line-height: 1; display: block; }
  .warranty-band {
    position: absolute; left: 46px; top: 1340px; width: 260px; height: 54px;
    background: var(--blue-bright); transform: rotate(1deg);
    font-family: "Montserrat", sans-serif; font-weight: 700; font-size: 26px;
    color: var(--navy); display: flex; align-items: center; justify-content: center;
    white-space: nowrap;
  }

  .sleeper-panel {
    position: absolute; left: 295px; top: 1185px; width: 360px; height: 228px;
    background: linear-gradient(90deg, var(--blue-bright), var(--blue));
    border-radius: 12px; transform: rotate(-1.5deg);
    text-align: center; color: var(--white); font-family: "Oswald", sans-serif; font-weight: 500;
    white-space: nowrap;
    display: flex; flex-direction: column; align-items: center; justify-content: center;
  }
  .sleeper-head { display: block; font-size: 56px; line-height: 1; letter-spacing: -0.5px; }
  .sleeper-list { display: block; font-size: 37px; line-height: 1.08; margin-top: 12px; letter-spacing: -0.5px; }
</style>
</head>
<body>
<main class="canvas">
  <section class="package-front">
    <div class="tagline-panel"></div>
    <div class="photo-hero" role="img" aria-label="Photo of a woman hugging a white pillow"></div>
    <div class="photo-cloud" role="img" aria-label="Soft white cloud illustration"></div>
    <h2 class="tagline">
      <span class="small">Like</span>
      <span class="large">Sleeping</span>
      <span class="large">On a Cloud</span>
    </h2>
    <svg class="tagline-rule" width="290" height="20" viewBox="0 0 290 20"><path d="M2 16 Q150 2 288 10" stroke="#fff" stroke-width="3" fill="none" stroke-linecap="round"/></svg>

    <div class="main-panel"></div>

    <div class="logo-panel">
      <span class="brand-name">Maple 3</span>
      <span class="brand-sub">pillows &amp; more...</span>
    </div>

    <h1 class="product-title">ADJUSTABLE<br>PILLOW</h1>

    <ul class="feature-list">
      <li class="feature">
        <span class="feature-icon">
          <svg width="34" height="34" viewBox="0 0 34 34" fill="none" stroke="#fff" stroke-width="2.5"><circle cx="17" cy="17" r="14"/><path d="M17 7v20M7 17h20M10 10l14 14M24 10L10 24"/></svg>
        </span>
        <div class="feature-title">Cool &amp; Anti-Bacterial</div>
        <div class="feature-text">Antimicrobial, ultra-soft &amp; cool to the touch cover</div>
      </li>
      <li class="feature">
        <span class="feature-icon">
          <svg width="36" height="30" viewBox="0 0 36 30" fill="none" stroke="#fff" stroke-width="2.5"><rect x="4" y="17" width="28" height="9" rx="4"/><path d="M6 12 Q18 2 30 12"/><path d="M24 6l6 6-7 2"/></svg>
        </span>
        <div class="feature-title">MapleComfort™ Memory Foam</div>
        <div class="feature-text">Provides cloud-like comfort &amp; support</div>
      </li>
      <li class="feature">
        <span class="feature-icon">
          <svg width="36" height="30" viewBox="0 0 36 30" fill="#fff"><rect x="3" y="6" width="3" height="20"/><rect x="3" y="18" width="30" height="4"/><rect x="30" y="18" width="3" height="8"/><circle cx="11" cy="14" r="3.5"/><rect x="16" y="11" width="16" height="6" rx="2"/></svg>
        </span>
        <div class="feature-title">Perfect For All Sleepers</div>
        <div class="feature-text">Fully Adjustable for all sleeping positions</div>
      </li>
      <li class="feature">
        <span class="feature-icon">
          <svg width="32" height="32" viewBox="0 0 32 32"><path d="M6 26 C6 12 14 6 27 5 C27 18 20 26 6 26Z" fill="#fff"/><path d="M6 26 L20 12" stroke="#0677BA" stroke-width="2"/></svg>
        </span>
        <div class="feature-title">Eco Friendly</div>
        <div class="feature-text">Hypoallergenic and PureFoam-Cert® certified</div>
      </li>
    </ul>

    <div class="size-tag">
      <span class="size-name">QUEEN SIZE</span>
      <span class="size-dims">20″ x 30″</span>
    </div>
    <div class="warranty-band">5.Year Warranty</div>

    <div class="sleeper-panel">
      <span class="sleeper-head">PERFECT FOR:</span>
      <span class="sleeper-list">BACK, SIDE OR<br>STOMACH SLEEPERS.</span>
    </div>
  </section>
</main>
</body>
</html>
```